Quirky Label Design for an Exciting UK-Based Organic Skincare Company!

We need label designs across our range of products, we are a high quality yet quirky organic skincare company called Gently Velvety, we use frosted glass packaging, and we are just wanting one design done for now, but the winning designer we would want to work with to design the rest of the labels for us. We also want them to design business cards and other literature at some point and maybe even a website page.

Our label design will go on a 63mm tall frosted glass jar which is 62mm in diameter. The actual label dimensions should be, 170 mm (W) x 50 mm (H). The idea is so that it wraps around the whole jar with the design at one side (at the front) and the ingredients on another (at the back).

LABEL 1
Organic Polynesian Whipped Body Butter
Vanilla Bean
120ml

Made with Organic Shea and Cocoa Butters and exotic Monoi de Tahiti

Ingredients (INCI): Organic Raw Shea Butter (Butyrospermum Parkii), Organic Raw Cocoa Butter (Theobroma Cacao), Monoi de Tahiti (Coconut (Cocos nucifera) oil (and) Tiare (Gardenia tahitensis) flower), Organic Sweet Almond Oil (Prunus Amygdalus Dulcis), Organic Madagascan Vanilla Extract (Vanillin)

Handmade by Gently Velvety Ltd
14 Larkwell Lane, Bournemouth BH3 9QT, UK
Batch:

OPTIONAL WRITING (if it fits in):
100% Natural and Organic
Intensely Moisturising

LABEL 2
Mango Smoothie
120ml

Ingredients (INCI): Organic Raw Shea Butter (Butyrospermum Parkii), Organic Raw Cocoa Butter (Theobroma Cacao), Monoi de Tahiti (Coconut (Cocos nucifera) oil (and) Tiare (Gardenia tahitensis) flower), Organic Sweet Almond Oil (Prunus Amygdalus Dulcis), Organic Mango Flavour (Aroma)

Batch:

100% Natural and Organic
Intensely Moisturising

I have attached a picture of the jar we use and the lid we use for these products, as well as our logo. I've also attached a 'Handmade in Dorset' stamp which we'd like to go on there if possible, along with a shelf life symbol.

I am thinking the background colour of the labels will be either white or even brown paper colour. Perhaps it would be interesting to see it in both. UPDATE: We have decided on white background now, not brown.

The final design should denote handmade, organic, high quality, pure, yet quirky and original / unique. I am thinking perhaps a seemingly hand-drawn black leaf outline? Could fit the bill, but as I say, up to you. Something that says handmade yet professional.

I'd like to have the original Photoshop files from the winning designer so we can use them as a template for the rest of our horizontal labels.
Updates

Project Deadline Extended
Reason: Just need a few more days for designs we like to be worked on further, and to review new designs!

Target Market(s)

Everyone that appreciates a good quality skincare product focusing on natural & organic. Price is mid-range to high

Industry/Entity Type

It Company

Requirements
Must have
• Must make the product look high quality & organic yet quirky and accessible. Must have our logo and the shelf life symbol and the writing as above.
Nice to have
• Nice to have the 'handmade' stamp attached, but not absolutely necessary if it doesn't fit within your design.

```html
<!DOCTYPE html>
<html lang="en">
<head>
<meta charset="utf-8">
<title>Gently Velvety – Organic Polynesian Whipped Body Butter labels</title>
<link rel="stylesheet" href="https://fonts.googleapis.com/css2?family=Teko:wght@500&family=Pinyon+Script&family=Short+Stack&family=Poppins:wght@400;600&display=swap">
<style>
  :root {
    --paper: #ffffff;
    --label-bg: #eef2ef;
    --ink: #3a3a3a;
    --logo-grey: #8a8a8a;
    --silver-dark: #5d5d5d;
    --silver-mid: #a9a9a9;
    --silver-light: #f2f2f2;
    --lime: #a8cf45;
    --teal: #4fa6b1;
    --blush: #f5aeb0;
    --gold: #d2a70b;
  }
  * { box-sizing: border-box; margin: 0; padding: 0; }
  html, body { width: 1200px; height: 1180px; overflow: hidden; background: var(--paper); }
  .sheet { position: relative; width: 1200px; height: 1180px; border: 1px solid #bdbdbd; }

  .label {
    position: absolute;
    width: 358px; height: 276px;
    background: var(--label-bg);
    border-radius: 4px;
    overflow: hidden;
    --accent: var(--lime);
  }
  .label--lime  { --accent: var(--lime);  left: 160px; top: 246px; }
  .label--teal  { --accent: var(--teal);  left: 646px; top: 235px; }
  .label--blush { --accent: var(--blush); left: 162px; top: 786px; }
  .label--gold  { --accent: var(--gold);  left: 650px; top: 787px; }

  .label__rule {
    position: absolute; top: 23px; height: 3px; background: var(--accent);
  }
  .label__rule--left  { left: 12px; width: 125px; }
  .label__rule--right { right: 0; width: 150px; }

  .label__badge {
    position: absolute; left: 22px; top: 9px;
    width: 30px; height: 30px; border-radius: 50%;
    background: var(--accent);
    color: #fff;
    font: 400 5px/1.2 "Poppins", sans-serif;
    text-align: center;
    display: flex; align-items: center; justify-content: center;
  }

  .label__brand {
    position: absolute; left: 137px; width: 71px; top: 12px;
    font: 600 10px/1.15 "Poppins", sans-serif;
    color: var(--logo-grey);
    text-align: center;
    text-transform: uppercase;
  }

  .label__title {
    position: absolute; left: 0; right: 0; top: 52px;
    font: 500 55px/1 "Teko", sans-serif;
    color: var(--accent);
    text-align: center;
    letter-spacing: 0.5px;
  }
  .label--lime .label__title {
    background: linear-gradient(90deg, #3f3f3f 0%, #555 40%, #d9d9d9 48%, #777 60%, #3f3f3f 100%);
    -webkit-background-clip: text; background-clip: text; color: transparent;
  }

  .label__subtitle {
    position: absolute; left: 0; right: 0; top: 106px;
    font: 400 17px/1 "Pinyon Script", cursive;
    color: #666;
    text-align: center;
  }

  .label__leaf {
    position: absolute; left: 170px; top: 132px;
    width: 28px; height: 38px;
    border-radius: 50% 50% 50% 50% / 60% 60% 40% 40%;
    background: var(--accent);
    opacity: 0.35;
  }

  .label__scent {
    position: absolute; left: 0; right: 0; top: 175px; height: 43px;
    background: linear-gradient(90deg, var(--silver-dark) 0%, var(--silver-light) 10%, var(--silver-mid) 22%, #6e6e6e 40%, var(--silver-light) 55%, #7a7a7a 72%, var(--silver-light) 85%, var(--silver-dark) 100%);
    font: 400 28px/43px "Short Stack", cursive;
    color: #fff;
    text-align: center;
    letter-spacing: 2px;
  }

  .label__panel {
    position: absolute; left: 0; right: 0; top: 218px; bottom: 0;
    background: var(--accent);
    text-align: center;
    color: var(--ink);
  }
  .label__claim {
    margin-top: 10px;
    font: 400 8px/1.35 "Poppins", sans-serif;
    text-transform: uppercase;
  }
  .label__volume {
    font: 500 20px/1 "Teko", sans-serif;
    margin-top: 2px;
  }
</style>
</head>
<body>
<main class="sheet">

  <section class="label label--lime">
    <span class="label__rule label__rule--left"></span>
    <span class="label__rule label__rule--right"></span>
    <span class="label__badge">100%<br>NATURAL</span>
    <p class="label__brand">Gently Velvety</p>
    <h2 class="label__title">Organic Polynesian</h2>
    <p class="label__subtitle">Whipped Body Butter</p>
    <span class="label__leaf" role="img" aria-label="Hand-drawn leaf outline"></span>
    <p class="label__scent">Vanilla Bean</p>
    <div class="label__panel">
      <p class="label__claim">Made with organic shea and cocoa butters<br>and exotic Monoi de Tahiti</p>
      <p class="label__volume">120ml</p>
    </div>
  </section>

  <section class="label label--teal">
    <span class="label__rule label__rule--left"></span>
    <span class="label__rule label__rule--right"></span>
    <span class="label__badge">100%<br>NATURAL</span>
    <p class="label__brand">Gently Velvety</p>
    <h2 class="label__title">Organic Polynesian</h2>
    <p class="label__subtitle">Whipped Body Butter</p>
    <span class="label__leaf" role="img" aria-label="Hand-drawn leaf outline"></span>
    <p class="label__scent">Vanilla Bean</p>
    <div class="label__panel">
      <p class="label__claim">Made with organic shea and cocoa butters<br>and exotic Monoi de Tahiti</p>
      <p class="label__volume">120ml</p>
    </div>
  </section>

  <section class="label label--blush">
    <span class="label__rule label__rule--left"></span>
    <span class="label__rule label__rule--right"></span>
    <span class="label__badge">100%<br>NATURAL</span>
    <p class="label__brand">Gently Velvety</p>
    <h2 class="label__title">Organic Polynesian</h2>
    <p class="label__subtitle">Whipped Body Butter</p>
    <span class="label__leaf" role="img" aria-label="Hand-drawn leaf outline"></span>
    <p class="label__scent">Vanilla Bean</p>
    <div class="label__panel">
      <p class="label__claim">Made with organic shea and cocoa butters<br>and exotic Monoi de Tahiti</p>
      <p class="label__volume">120ml</p>
    </div>
  </section>

  <section class="label label--gold">
    <span class="label__rule label__rule--left"></span>
    <span class="label__rule label__rule--right"></span>
    <span class="label__badge">100%<br>NATURAL</span>
    <p class="label__brand">Gently Velvety</p>
    <h2 class="label__title">Organic Polynesian</h2>
    <p class="label__subtitle">Whipped Body Butter</p>
    <span class="label__leaf" role="img" aria-label="Hand-drawn leaf outline"></span>
    <p class="label__scent">Vanilla Bean</p>
    <div class="label__panel">
      <p class="label__claim">Made with organic shea and cocoa butters<br>and exotic Monoi de Tahiti</p>
      <p class="label__volume">120ml</p>
    </div>
  </section>

</main>
</body>
</html>
```